Restaurant service company needs a website!

I am looking for a skilled web designer/developer to create a professional, responsive, and easy-to-navigate website for my company, which specializes in servicing restaurant cooking equipment. The site should communicate trust, reliability, and technical expertise to our target audience, restaurant owners, managers, and commercial kitchen operators. I have included the company logos, if any other format for them is needed please let me know.

Target Market(s)

restaurant owners, managers, and commercial kitchen operators

Industry/Entity Type

Commercial Kitchen Equipment Service

Coding

Coded - Design and coding required

Number of Pages Required

1 page

Font styles to use
Serif
Sans Serif

Requirements
Must have
• Contact and service request forms, Click-to-call functionality for mobile, Clean, modern layout with strong visuals, Easy navigation, mobile-friendly
Nice to have
• Testimonials or Reviews, If possible a click-to-text functionality for mobile.
Should not have
• Any mention of Refrigeration or HVAC, "Free Quotes"

```html
<!DOCTYPE html>
<html lang="en">
<head>
<meta charset="utf-8">
<title>Ironbridge Kitchen Service</title>
<link href="https://fonts.googleapis.com/css2?family=Lexend:wght@400;500;600;700&family=Lato:ital,wght@0,400;0,700;1,400&display=swap" rel="stylesheet">
<style>
:root{
  --red:#dc2626;
  --red-dark:#c81e1e;
  --red-soft:#fee2e2;
  --ink:#111827;
  --text:#374151;
  --muted:#6b7280;
  --line:#e5e7eb;
  --light:#f9fafb;
  --navy:#111827;
  --white:#fff;
  --star:#facc15;
}
*{box-sizing:border-box;margin:0;padding:0}
html,body{width:1200px;height:3470px;overflow:hidden}
body{font-family:"Lato",sans-serif;color:var(--text);background:var(--white);position:relative}
h1,h2,h3,h4,.head{font-family:"Lexend",sans-serif;color:var(--ink)}
.wrap{width:760px;margin:0 auto;position:relative}
svg.ic{width:12px;height:12px;stroke:currentColor;fill:none;stroke-width:2;stroke-linecap:round;stroke-linejoin:round}

/* nav */
.nav{height:40px;display:flex;align-items:center;justify-content:space-between;padding:0 220px 0 215px;background:var(--white);border-bottom:1px solid var(--line)}
.brand{font-family:"Lexend",sans-serif;font-weight:700;font-size:15px;color:#134e5e;display:flex;align-items:center;gap:6px;letter-spacing:.5px}
.brand i{width:10px;height:10px;background:#134e5e;display:block}
.nav ul{display:flex;gap:20px;list-style:none;align-items:center;font-size:11px;color:var(--text)}
.btn-call{background:var(--red);color:var(--white);font-size:11px;font-weight:700;padding:6px 12px;border-radius:4px;display:flex;gap:6px;align-items:center}

/* hero */
.hero{height:470px;position:relative;text-align:center;color:var(--white);background:linear-gradient(180deg,#5a5b5e 0%,#3e3f43 45%,#2c2c2f 100%)}
.hero::after{content:"";position:absolute;inset:0;background:rgba(0,0,0,.35)}
.hero>*{position:relative;z-index:1}
.hero h1{color:var(--white);font-size:37px;line-height:37px;font-weight:700;padding-top:82px}
.hero h1 span{color:var(--red);display:block}
.hero p{font-size:16px;line-height:20px;width:480px;margin:22px auto 0;color:#e5e7eb}
.hero-btns{display:flex;justify-content:center;gap:8px;margin-top:20px}
.hbtn{height:37px;padding:0 20px;display:flex;align-items:center;gap:8px;font-size:11px;font-weight:700;border-radius:4px}
.hbtn.red{background:var(--red)}
.hbtn.ghost{border:2px solid var(--white)}
.stats{display:flex;justify-content:center;gap:0;margin-top:24px}
.stat{width:260px}
.stat b{display:block;color:var(--red);font-family:"Lexend",sans-serif;font-size:18px}
.stat small{font-size:11px;color:#e5e7eb}

/* sections */
.sec-title{text-align:center;font-size:22px;font-weight:600}
.sec-sub{text-align:center;font-size:12.5px;color:var(--muted);line-height:17px;margin:10px auto 0;width:440px}
.services{height:748px;background:var(--light);padding-top:52px}
.grid3{display:grid;grid-template-columns:repeat(3,240px);gap:20px 20px;margin-top:38px}
.card{background:var(--white);border-radius:6px;overflow:hidden;height:260px;box-shadow:0 2px 8px rgba(0,0,0,.08)}
.ph{height:117px}
.card .body{padding:14px}
.icon-box{width:28px;height:28px;border-radius:5px;background:var(--red-soft);color:var(--red);display:flex;align-items:center;justify-content:center}
.card h3{font-size:12px;font-weight:500;margin:12px 0 8px}
.card p{font-size:9.5px;line-height:16px;color:var(--muted)}

.why{height:618px;padding-top:50px}
.why h2{font-size:22px;font-weight:600;width:360px;line-height:24px}
.why .lead{font-size:12px;line-height:17px;color:var(--muted);width:360px;margin-top:14px}
.feat{display:flex;gap:10px;margin-top:14px;width:365px}
.feat .icon-box{width:24px;height:24px;flex:none}
.feat h4{font-size:11px;font-weight:500;margin-bottom:5px}
.feat p{font-size:9px;line-height:15px;color:var(--muted)}
.why-photo{position:absolute;left:395px;top:50px;width:365px;height:395px;border-radius:6px;box-shadow:0 10px 30px rgba(0,0,0,.15)}
.badge{position:absolute;left:380px;top:397px;width:84px;height:62px;background:var(--red);color:var(--white);border-radius:6px;padding:12px 15px}
.badge b{font-family:"Lexend",sans-serif;font-size:15px;display:block}
.badge small{font-size:8.5px}

.request{height:634px;background:var(--light);padding-top:52px}
.form-card{width:520px;height:453px;margin:28px auto 0;display:flex;border-radius:6px;overflow:hidden;box-shadow:0 4px 18px rgba(0,0,0,.1)}
.form{width:260px;background:var(--white);padding:30px 30px}
.row{display:flex;gap:14px;margin-bottom:14px}
.fld{flex:1}
.fld label{display:block;font-size:8px;font-weight:700;color:var(--text);margin-bottom:8px}
.in{height:27px;border:1px solid #d1d5db;border-radius:4px;font-size:7.5px;color:#9ca3af;padding:0 10px;display:flex;align-items:center;justify-content:space-between}
.ta{height:64px;align-items:flex-start;padding-top:9px;line-height:12px}
.count{font-size:6.5px;color:var(--muted);margin:6px 0 14px}
.submit{height:36px;background:var(--red);color:var(--white);border-radius:4px;font-size:10.5px;font-weight:700;display:flex;align-items:center;justify-content:center;margin-top:16px}
.help{flex:1;background:var(--red);color:var(--white);padding:30px 30px}
.help h3{color:var(--white);font-size:14px;font-weight:600;margin-bottom:18px}
.hitem{display:flex;gap:12px;margin-bottom:22px;font-size:9px;line-height:15px}
.hitem .hi{width:24px;height:24px;border-radius:5px;background:rgba(255,255,255,.2);display:flex;align-items:center;justify-content:center;flex:none}
.hitem b{display:block}
.promise{background:rgba(255,255,255,.18);border-radius:5px;padding:12px 10px;font-size:7.5px;line-height:12px;margin-top:8px}
.promise b{display:block;font-size:9px;margin-bottom:6px}

.testis{height:593px;padding-top:52px}
.grid4{display:grid;grid-template-columns:repeat(4,175px);gap:20px;margin-top:38px}
.tcard{height:196px;background:var(--white);border-radius:6px;box-shadow:0 2px 10px rgba(0,0,0,.09);padding:15px 15px}
.stars{color:var(--star);font-size:10px;letter-spacing:1px}
.tcard q{display:block;font-style:italic;font-size:9px;line-height:15px;color:var(--muted);margin-top:8px;height:108px}
.who{display:flex;gap:10px;align-items:flex-start}
.av{width:28px;height:28px;border-radius:50%;background:linear-gradient(135deg,#9ca3af,#4b5563);flex:none}
.who b{font-size:9.5px;font-weight:700;color:var(--ink);display:block}
.who small{font-size:8px;color:var(--muted);line-height:12px;display:block}
.cta{height:169px;background:var(--red);border-radius:8px;margin-top:39px;text-align:center;color:var(--white);padding-top:34px}
.cta h2{color:var(--white);font-size:18px;font-weight:600}
.cta p{font-size:11.5px;margin-top:12px;color:#fde2e2}
.cta-btns{display:flex;justify-content:center;gap:12px;margin-top:20px}
.cbtn{height:38px;padding:0 20px;border-radius:4px;font-size:10.5px;font-weight:700;display:flex;align-items:center}
.cbtn.w{background:var(--white);color:var(--red)}
.cbtn.o{border:2px solid var(--white)}

.footer{height:274px;background:var(--navy);color:#d1d5db;padding-top:40px}
.fcols{display:flex}
.fcol1{width:390px}
.fcol2{width:195px}
.fcol1 .brand{color:var(--white)}
.fcol1 .brand i{background:var(--white)}
.fcol1 p{font-size:9px;line-height:15px;margin-top:16px;width:280px}
.fcontact{display:flex;gap:16px;font-size:9px;margin-top:16px;color:var(--white)}
.fcontact span{display:flex;gap:5px;align-items:center}
.fcontact svg{color:var(--red)}
.footer h4{color:var(--white);font-size:10px;font-weight:500;margin-bottom:14px}
.footer li{list-style:none;font-size:9px;margin-bottom:9px}
.fci{display:flex;gap:6px;font-size:9px;line-height:13px;margin-bottom:11px}
.fci svg{color:var(--red);margin-top:1px}
.fci b{color:var(--white);font-weight:400;display:block}
.fbottom{border-top:1px solid #374151;margin-top:42px;padding-top:20px;display:flex;justify-content:space-between;align-items:center;font-size:8px;color:#9ca3af}
</style>
</head>
<body>

<nav class="nav">
  <div class="brand"><i></i>IRONBRIDGE</div>
  <ul>
    <li>Services</li><li>About Us</li><li>Contact</li>
    <li class="btn-call"><svg class="ic" viewBox="0 0 24 24"><path d="M5 3h4l2 5-3 2a11 11 0 0 0 6 6l2-3 5 2v4a2 2 0 0 1-2 2A17 17 0 0 1 3 5a2 2 0 0 1 2-2z"/></svg>Call Now</li>
  </ul>
</nav>

<header class="hero" role="img" aria-label="Stainless steel commercial kitchen with ovens and work tables">
  <h1>Professional Commercial<span>Kitchen Equipment</span>Service &amp; Repair</h1>
  <p>Expert technicians providing reliable maintenance, emergency repairs, and preventive care for your restaurant's cooking equipment. Minimize downtime, maximize efficiency.</p>
  <div class="hero-btns">
    <div class="hbtn red"><svg class="ic" viewBox="0 0 24 24"><path d="M5 3h4l2 5-3 2a11 11 0 0 0 6 6l2-3 5 2v4a2 2 0 0 1-2 2A17 17 0 0 1 3 5a2 2 0 0 1 2-2z"/></svg>Emergency Service: (555) 014-2280</div>
    <div class="hbtn ghost">Schedule Service</div>
  </div>
  <div class="stats">
    <div class="stat"><b>24/7</b><small>Emergency Service</small></div>
    <div class="stat"><b>15+</b><small>Years Experience</small></div>
    <div class="stat"><b>500+</b><small>Satisfied Clients</small></div>
  </div>
</header>

<section class="services">
  <h2 class="sec-title">Our Professional Services</h2>
  <p class="sec-sub">Comprehensive commercial kitchen equipment services designed to keep your restaurant running at peak performance</p>
  <div class="wrap grid3">
    <div class="card"><div class="ph" role="img" aria-label="Technician repairing a commercial oven" style="background:linear-gradient(135deg,#c9ccd1,#6b7280)"></div><div class="body"><div class="icon-box"><svg class="ic" viewBox="0 0 24 24"><path d="M5 5l14 14M19 5L5 19"/></svg></div><h3>Equipment Repair</h3><p>Expert repair services for all types of commercial cooking equipment including ovens, grills, fryers, and more.</p></div></div>
    <div class="card"><div class="ph" role="img" aria-label="Maintenance checklist on a clipboard in a kitchen" style="background:linear-gradient(135deg,#a8a29e,#44403c)"></div><div class="body"><div class="icon-box"><svg class="ic" viewBox="0 0 24 24"><rect x="4" y="5" width="16" height="15" rx="2"/><path d="M4 10h16M9 3v4M15 3v4"/></svg></div><h3>Preventive Maintenance</h3><p>Regular maintenance programs to prevent breakdowns and extend equipment life, keeping your kitchen running smoothly.</p></div></div>
    <div class="card"><div class="ph" role="img" aria-label="Emergency service van parked outside" style="background:linear-gradient(135deg,#e5e7eb,#9ca3af 60%,#ea8a3a)"></div><div class="body"><div class="icon-box"><svg class="ic" viewBox="0 0 24 24"><circle cx="12" cy="12" r="8"/><path d="M12 8v4l3 2"/></svg></div><h3>24/7 Emergency Service</h3><p>Round-the-clock emergency repair service to minimize downtime and keep your restaurant operational.</p></div></div>
    <div class="card"><div class="ph" role="img" aria-label="Technician installing a range under an exhaust hood" style="background:linear-gradient(135deg,#d1d5db,#4b5563)"></div><div class="body"><div class="icon-box"><svg class="ic" viewBox="0 0 24 24"><circle cx="12" cy="12" r="3"/><circle cx="12" cy="12" r="8"/></svg></div><h3>Installation &amp; Setup</h3><p>Professional installation and setup of new commercial kitchen equipment with proper calibration and testing.</p></div></div>
    <div class="card"><div class="ph" role="img" aria-label="Inspector in a chef coat checking kitchen equipment" style="background:linear-gradient(135deg,#b8bcc2,#374151)"></div><div class="body"><div class="icon-box"><svg class="ic" viewBox="0 0 24 24"><path d="M12 3l7 3v6c0 4-3 7-7 9-4-2-7-5-7-9V6z"/><path d="M9 12l2 2 4-4"/></svg></div><h3>Safety Inspections</h3><p>Comprehensive safety inspections and compliance checks to ensure your equipment meets all regulations.</p></div></div>
    <div class="card"><div class="ph" role="img" aria-label="Technicians reviewing paperwork in a kitchen" style="background:linear-gradient(135deg,#9ca3af,#3f3f46)"></div><div class="body"><div class="icon-box"><svg class="ic" viewBox="0 0 24 24"><path d="M5 14v-2a7 7 0 0 1 14 0v2"/><rect x="4" y="14" width="4" height="5" rx="1"/><rect x="16" y="14" width="4" height="5" rx="1"/></svg></div><h3>Technical Support</h3><p>Expert technical consultation and support to optimize your kitchen operations and equipment performance.</p></div></div>
  </div>
</section>

<section class="why">
  <div class="wrap">
    <h2>Why Restaurant Owners Choose Us</h2>
    <p class="lead">With over 15 years of experience serving the commercial kitchen industry, we've built our reputation on reliability, expertise, and exceptional customer service.</p>
    <div class="feat"><div class="icon-box"><svg class="ic" viewBox="0 0 24 24"><circle cx="12" cy="8" r="4"/><path d="M5 20c1-4 13-4 14 0"/></svg></div><div><h4>Certified Technicians</h4><p>Our team consists of factory-trained and certified professionals with extensive experience in commercial kitchen equipment.</p></div></div>
    <div class="feat"><div class="icon-box"><svg class="ic" viewBox="0 0 24 24"><circle cx="12" cy="12" r="7"/><path d="M12 9v3"/></svg></div><div><h4>Fast Response Time</h4><p>We understand the urgency of equipment failures. Our average response time is under 2 hours for emergency calls.</p></div></div>
    <div class="feat"><div class="icon-box"><svg class="ic" viewBox="0 0 24 24"><path d="M4 12l8-8h8v8l-8 8z"/></svg></div><div><h4>Transparent Pricing</h4><p>No hidden fees or surprise charges. We provide upfront pricing with detailed estimates before any work begins.</p></div></div>
    <div class="feat"><div class="icon-box"><svg class="ic" viewBox="0 0 24 24"><circle cx="12" cy="9" r="5"/><path d="M9 14l-1 7 4-2 4 2-1-7"/></svg></div><div><h4>Quality Guarantee</h4><p>All our repairs come with a comprehensive warranty. We stand behind our work with a 100% satisfaction guarantee.</p></div></div>
    <div class="feat"><div class="icon-box"><svg class="ic" viewBox="0 0 24 24"><path d="M6 6l12 12M18 6L6 18"/></svg></div><div><h4>Advanced Equipment</h4><p>We use state-of-the-art diagnostic tools and genuine OEM parts to ensure lasting repairs and optimal performance.</p></div></div>
    <div class="feat"><div class="icon-box"><svg class="ic" viewBox="0 0 24 24"><path d="M5 14v-2a7 7 0 0 1 14 0v2"/><rect x="4" y="14" width="4" height="5" rx="1"/><rect x="16" y="14" width="4" height="5" rx="1"/></svg></div><div><h4>Ongoing Support</h4><p>Post-service support and maintenance advice to help you get the most out of your equipment investment.</p></div></div>
    <div class="why-photo" role="img" aria-label="Team of service technicians in a commercial kitchen" style="background:linear-gradient(160deg,#a1a1aa,#52525b 60%,#3f3f46)"></div>
    <div class="badge"><b>500+</b><small>Happy Clients</small></div>
  </div>
</section>

<section class="request">
  <h2 class="sec-title">Request Service Today</h2>
  <p class="sec-sub" style="width:560px">Fill out the form below and we'll contact you within 30 minutes to schedule your service</p>
  <div class="form-card">
    <div class="form">
      <div class="row"><div class="fld"><label>Full Name *</label><div class="in">Enter your full nam</div></div><div class="fld"><label>Phone Number *</label><div class="in">(555) 123-4567</div></div></div>
      <div class="row"><div class="fld"><label>Email Address *</label><div class="in">your@email.com</div></div><div class="fld"><label>Restaurant Name *</label><div class="in">Your restaurant na</div></div></div>
      <div class="row"><div class="fld"><label>Equipment Type *</label><div class="in" style="color:var(--ink)">Select equipi<span>▾</span></div></div><div class="fld"><label>Urgency Level *</label><div class="in" style="color:var(--ink)">Select urgen<span>▾</span></div></div></div>
      <div class="fld"><label>Issue Description *</label><div class="in ta">Please describe the issue you're experiencing...</div></div>
      <div class="count">0/500 characters</div>
      <div class="fld"><label>Preferred Service Time</label><div class="in">e.g., Tomorrow morning, This weekend, ASAP</div></div>
      <div class="submit">Submit Service Request</div>
    </div>
    <div class="help">
      <h3>Need Immediate Help?</h3>
      <div class="hitem"><div class="hi"><svg class="ic" viewBox="0 0 24 24"><path d="M5 3h4l2 5-3 2a11 11 0 0 0 6 6l2-3 5 2v4a2 2 0 0 1-2 2A17 17 0 0 1 3 5a2 2 0 0 1 2-2z"/></svg></div><div><b>Emergency Hotline</b>(555) 014-2280<br>Available 24/7</div></div>
      <div class="hitem"><div class="hi"><svg class="ic" viewBox="0 0 24 24"><rect x="3" y="5" width="18" height="14" rx="2"/><path d="M3 7l9 6 9-6"/></svg></div><div><b>Email Support</b>service@ironbridgekitchen.com<br>Response within 1 hour</div></div>
      <div class="hitem"><div class="hi"><svg class="ic" viewBox="0 0 24 24"><circle cx="12" cy="12" r="8"/><path d="M12 8v4l3 2"/></svg></div><div><b>Response Time</b>Emergency: &lt;2 hours<br>Standard: Same day</div></div>
      <div class="hitem"><div class="hi"><svg class="ic" viewBox="0 0 24 24"><path d="M12 21s-6-6-6-11a6 6 0 0 1 12 0c0 5-6 11-6 11z"/><circle cx="12" cy="10" r="2"/></svg></div><div><b>Service Area</b>Greater Metro Area<br>50-mile radius</div></div>
      <div class="promise"><b>Emergency Service Promise</b>We understand equipment failures can cost you money. That's why we guarantee emergency response within 2 hours, 24/7.</div>
    </div>
  </div>
</section>

<section class="testis">
  <h2 class="sec-title">What Our Clients Say</h2>
  <p class="sec-sub" style="width:640px">Don't just take our word for it - hear from restaurant owners and managers who trust us with their equipment</p>
  <div class="wrap">
    <div class="grid4">
      <div class="tcard"><div class="stars">★★★★★</div><q>Ironbridge saved our busy Friday night when our main grill went down. They had a technician here within an hour and got us back up and running. Exceptional service!</q><div class="who"><div class="av" role="img" aria-label="Client portrait"></div><div><b>Dana Whitlock</b><small>Owner, Lantern House Restaurant</small></div></div></div>
      <div class="tcard"><div class="stars">★★★★★</div><q>We've been using Ironbridge for our preventive maintenance program for 3 years. Our equipment runs better and lasts longer. Their technicians are knowledgeable and professional.</q><div class="who"><div class="av" role="img" aria-label="Client portrait"></div><div><b>Marco Delgado</b><small>Kitchen Manager, Corner Plate Bistro</small></div></div></div>
      <div class="tcard"><div class="stars">★★★★★</div><q>The team at Ironbridge is incredibly reliable. They fixed our ice machine and dishwasher the same day, and their pricing was very fair. Highly recommend their services.</q><div class="who"><div class="av" role="img" aria-label="Client portrait"></div><div><b>Laura Bennett</b><small>General Manager, Main Street Grill</small></div></div></div>
      <div class="tcard"><div class="stars">★★★★★</div><q>When our commercial oven broke during dinner rush, Ironbridge came to our rescue. Fast, professional, and they use quality parts. They've earned our trust and business.</q><div class="who"><div class="av" role="img" aria-label="Client portrait"></div><div><b>Vince Carraro</b><small>Owner, Nonna's Table</small></div></div></div>
    </div>
    <div class="cta">
      <h2>Join 500+ Satisfied Restaurant Owners</h2>
      <p>Experience the reliability and expertise that keeps kitchens running smoothly across the metro area</p>
      <div class="cta-btns"><div class="cbtn w">Call for Emergency Service</div><div class="cbtn o">Schedule Service Online</div></div>
    </div>
  </div>
</section>

<footer class="footer">
  <div class="wrap">
    <div class="fcols">
      <div class="fcol1">
        <div class="brand"><i></i>IRONBRIDGE</div>
        <p>Professional commercial kitchen equipment service and repair. Expert technicians providing reliable maintenance, emergency repairs, and preventive care for restaurants across the metro area.</p>
        <div class="fcontact"><span><svg class="ic" viewBox="0 0 24 24"><path d="M5 3h4l2 5-3 2a11 11 0 0 0 6 6l2-3 5 2v4a2 2 0 0 1-2 2A17 17 0 0 1 3 5a2 2 0 0 1 2-2z"/></svg>(555) 014-2280</span><span><svg class="ic" viewBox="0 0 24 24"><rect x="3" y="5" width="18" height="14" rx="2"/><path d="M3 7l9 6 9-6"/></svg>service@ironbridgekitchen.com</span></div>
      </div>
      <div class="fcol2">
        <h4>Our Services</h4>
        <ul><li>Equipment Repair</li><li>Preventive Maintenance</li><li>24/7 Emergency Service</li><li>Installation &amp; Setup</li><li>Safety Inspections</li><li>Technical Support</li></ul>
      </div>
      <div>
        <h4>Contact Info</h4>
        <div class="fci"><svg class="ic" viewBox="0 0 24 24"><path d="M5 3h4l2 5-3 2a11 11 0 0 0 6 6l2-3 5 2v4a2 2 0 0 1-2 2A17 17 0 0 1 3 5a2 2 0 0 1 2-2z"/></svg><div><b>Emergency Hotline</b>(555) 014-2280</div></div>
        <div class="fci"><svg class="ic" viewBox="0 0 24 24"><circle cx="12" cy="12" r="8"/><path d="M12 8v4l3 2"/></svg><div><b>Response Time</b>&lt;2 hours emergency</div></div>
        <div class="fci"><svg class="ic" viewBox="0 0 24 24"><path d="M12 21s-6-6-6-11a6 6 0 0 1 12 0c0 5-6 11-6 11z"/><circle cx="12" cy="10" r="2"/></svg><div><b>Service Area</b>50-mile metro radius</div></div>
      </div>
    </div>
    <div class="fbottom"><span>© 2024 Ironbridge Kitchen Equipment Service. All rights reserved.</span><span class="btn-call" style="font-size:9px"><svg class="ic" viewBox="0 0 24 24"><path d="M5 3h4l2 5-3 2a11 11 0 0 0 6 6l2-3 5 2v4a2 2 0 0 1-2 2A17 17 0 0 1 3 5a2 2 0 0 1 2-2z"/></svg>Call Now</span></div>
  </div>
</footer>

</body>
</html>
```